Design Our Holiday Magic Coupon

Purpose - The purpose of this project is to create a festive, uplifting, and visually engaging physical coupon that will be mailed to our existing community and warm leads.
The intent is twofold: first, to spark delight and connection by offering a tangible, personal touch during the holiday season; and second, to encourage customers to explore and purchase our programs as they prepare for a strong start to 2026. This mailer is designed to re-engage past buyers, inspire current participants, and gently invite new momentum into their practice through a simple, friendly offer.

Project Description + Scope

This project includes the design and production of a printed coupon ( card format) featuring a 20% discount on purchases of $79 or more. The copy should feel warm, clear, and celebratory without urgency or pressure.

The front of the card will include the headline (“Live Your Best 2026”), bold discount information, and the coupon code FESTIVE20. The back will include a short message reinforcing the tone of possibility and ease, plus simple redemption instructions and the expiry date: December 31, 2025. Deliverables include print-ready artwork, color selection aligned with KH brand style.

one side
LIVE YOUR BEST 2026
Enjoy 20% OFF when you buy $79 or more.
Use code: FESTIVE20
Redeem until end of day December 31, 2025.

Back side - Move with clarity.
Heal with intelligence.
Lead with ease.
Thank you for being part of Kinetic Harmony.
Lots of love, Mara and the whole of Team Mara

Target Market(s)

yoga teachers, yoga lovers, mostly over 50 years, women

Font styles to use
Other font styles liked:
• see attached for feel

Colors
0054AA
0677BA
7BADD7
CADEEF
E8F1F8
0094D4
00A9DD
6FCCEA
C7EBF8
E9F6FB
00AB8E
00BBA5
67D7C9
C6EFE9
E9F9F6
EB3D1F
EC4F4E
F09395
F8D3D4
FCEDEE

Requirements
Nice to have
• see attached

```html
<!DOCTYPE html>
<html lang="en">
<head>
<meta charset="utf-8">
<title>Kinetic Harmony – Holiday Coupon</title>
<link rel="stylesheet" href="https://fonts.googleapis.com/css2?family=Montserrat:ital,wght@0,400;0,500;0,700;0,800;0,900;1,800&display=swap">
<style>
  :root {
    --brand-blue: #0054AA;
    --mid-blue: #0677BA;
    --sky-blue: #0094D4;
    --soft-blue: #7BADD7;
    --mint: #67D7C9;
    --white: #ffffff;
    --page: #ffffff;
  }
  * { box-sizing: border-box; margin: 0; padding: 0; }
  html, body {
    width: 1200px; height: 954px; overflow: hidden;
    background: var(--page);
    font-family: "Montserrat", Arial, sans-serif;
    color: var(--white);
  }
  .canvas { position: relative; width: 1200px; height: 954px; }

  .card { position: absolute; width: 523px; height: 865px; overflow: hidden; }
  .card--front { left: 56px; top: 45px; background: linear-gradient(170deg, var(--brand-blue) 0%, var(--mid-blue) 45%, var(--sky-blue) 100%); }
  .card--back { left: 621px; top: 42px; background: var(--brand-blue); }

  .decor { position: absolute; border-radius: 50%; }
  .decor--soft { background: radial-gradient(circle, rgba(123,173,215,0.28) 0%, rgba(123,173,215,0) 70%); }

  .brand { position: absolute; display: flex; align-items: center; gap: 14px; }
  .brand__dot { width: 62px; height: 62px; border-radius: 50%; background: var(--white); flex: none; }
  .brand__name { font-weight: 400; font-size: 33px; line-height: 0.95; letter-spacing: 0.5px; }
  .card--front .brand { left: 128px; top: 60px; }
  .card--back .brand { left: 127px; top: 86px; }

  .headline {
    position: absolute; left: 0; width: 100%; top: 163px;
    text-align: center; font-weight: 900; font-size: 68px; line-height: 73px; letter-spacing: -0.5px;
  }

  .rule { position: absolute; left: 0; width: 100%; top: 359px; height: 4px; background: var(--mint); }
  .badge {
    position: absolute; left: 163px; top: 328px; width: 197px; height: 67px;
    background: var(--mint); text-align: center;
    font-weight: 900; font-size: 48px; line-height: 67px; letter-spacing: 0.5px;
  }

  .discount {
    position: absolute; left: 0; width: 100%; text-align: center; font-weight: 900; letter-spacing: -8px;
  }
  .discount--value { top: 392px; font-size: 196px; line-height: 200px; }
  .discount--off { top: 552px; font-size: 190px; line-height: 200px; letter-spacing: -4px; }

  .condition {
    position: absolute; left: 0; width: 100%; top: 733px; text-align: center;
    font-size: 22px; font-weight: 500; letter-spacing: 0.2px;
  }
  .condition strong, .code strong, .expiry strong { font-weight: 800; }

  .code {
    position: absolute; left: 94px; top: 764px; width: 336px; height: 48px;
    background: var(--mint); border-radius: 12px; text-align: center;
    font-size: 25px; line-height: 48px; font-weight: 400;
  }
  .expiry {
    position: absolute; left: 0; width: 100%; top: 830px; text-align: center;
    font-size: 17px; font-weight: 500;
  }

  .values { position: absolute; left: 0; top: 0; width: 100%; height: 100%; }
  .values__line { position: absolute; background: var(--white); }
  .values__line--h { left: 42px; width: 437px; height: 1.5px; }
  .values__line--v { top: 238px; height: 266px; width: 1.5px; }
  .values__item {
    position: absolute; left: 0; width: 100%; text-align: center;
    font-size: 29px; font-weight: 400; letter-spacing: 0.3px;
  }
  .values__item em { font-style: italic; font-weight: 800; }

  .thanks {
    position: absolute; left: 0; width: 100%; top: 556px; text-align: center;
    font-size: 16.5px; line-height: 29px; font-weight: 500; letter-spacing: 0.3px;
  }
  .signoff {
    position: absolute; left: 0; width: 100%; top: 628px; text-align: center;
    font-size: 25px; line-height: 33.5px; font-weight: 500;
  }
  .signoff strong { font-weight: 800; }
  .accent { position: absolute; left: 207px; top: 816px; width: 109px; height: 2px; background: var(--mint); }
</style>
</head>
<body>
<main class="canvas">

  <section class="card card--front">
    <div class="decor decor--soft" style="left:-60px;top:60px;width:170px;height:200px" role="img" aria-label="Faint swirl decoration"></div>
    <div class="decor decor--soft" style="left:420px;top:-40px;width:160px;height:170px" role="img" aria-label="Faint swirl decoration"></div>
    <div class="decor decor--soft" style="left:-50px;top:560px;width:160px;height:180px" role="img" aria-label="Faint swirl decoration"></div>
    <div class="decor decor--soft" style="left:430px;top:440px;width:150px;height:200px" role="img" aria-label="Faint swirl decoration"></div>

    <div class="brand">
      <span class="brand__dot"></span>
      <span class="brand__name">kinetic<br>harmony</span>
    </div>

    <h1 class="headline">LIVE YOUR<br>BEST 2026</h1>

    <div class="rule"></div>
    <div class="badge">ENJOY</div>

    <div class="discount discount--value">20%</div>
    <div class="discount discount--off">OFF</div>

    <p class="condition">WHEN YOU <strong>BUY $79 OR MORE</strong></p>
    <p class="code">USE CODE: <strong>FESTIVE20</strong></p>
    <p class="expiry">Redeem until end of day <strong>December 31, 2025.</strong></p>
  </section>

  <section class="card card--back">
    <div class="decor decor--soft" style="left:-60px;top:40px;width:160px;height:200px" role="img" aria-label="Faint swirl decoration"></div>
    <div class="decor decor--soft" style="left:420px;top:-30px;width:160px;height:180px" role="img" aria-label="Faint swirl decoration"></div>
    <div class="decor decor--soft" style="left:-60px;top:680px;width:160px;height:200px" role="img" aria-label="Faint swirl decoration"></div>
    <div class="decor decor--soft" style="left:420px;top:660px;width:160px;height:200px" role="img" aria-label="Faint swirl decoration"></div>

    <div class="brand">
      <span class="brand__dot"></span>
      <span class="brand__name">kinetic<br>harmony</span>
    </div>

    <div class="values">
      <span class="values__line values__line--h" style="top:262px"></span>
      <span class="values__line values__line--h" style="top:332px"></span>
      <span class="values__line values__line--h" style="top:406px"></span>
      <span class="values__line values__line--h" style="top:481px"></span>
      <span class="values__line values__line--v" style="left:57px"></span>
      <span class="values__line values__line--v" style="left:463px"></span>
      <p class="values__item" style="top:280px">Move with <em>clarity.</em></p>
      <p class="values__item" style="top:356px">Heal with <em>Intelligence.</em></p>
      <p class="values__item" style="top:427px"><em>Lead</em> With <em>Ease.</em></p>
    </div>

    <p class="thanks">THANK YOU FOR<br>BEING PART OF KINETIC HARMONY.</p>
    <p class="signoff"><strong>LOTS OF LOVE,</strong><br><strong>MARA</strong> AND THE WHOLE<br>OF <strong>TEAM MARA</strong></p>
    <div class="accent"></div>
  </section>

</main>
</body>
</html>
```